Riverline Estate Holdings Co.

We need a logo and business card design for a Hong Kong based real estate company, KDT Land. We are want the brand to reflect the owners forward thinking, creative, and trend setting projects, while also reflecting a sense of security and strength. We invest in industrial properties which we convert to co-living or co-working spaces. KDT stands for Greater Bay Area which is the region around southern China including HK, Macau, and 9 other Chinese cities...made up of approx. 68 million people. There are massive infrastructure projects including the bridge to Macau and high-speed rail to SZ and the bridge connecting SZ and Zhongshan.

Target Market(s)

Chinese and western retail investors, as well as institutional investors

Industry/Entity Type

Real Estate Development

Contact Information for Business Card

Owen Tallis
CEO
owen@kdtland-hq.com
M + 852 9416 2057
F + 852 3582 0400
Suite 2207, The Meridale, 41 Larchmont Rd., Central, Hong Kong

Logo Text

kdt land (company name) lifestyle property development (underneath)

Colors

Designer to choose colors to be used in the design.

Requirements
Must have
• Details listed above. One side should include the logo and company name...kdt land in modern, hip styling with "lifestyle property development"
Nice to have
• Could be a Black card, with metallic purple "kdt" and white "land"...but open great design ideas
Should not have
• boring and traditional layout

```html
<!DOCTYPE html>
<html lang="en">
<head>
<meta charset="utf-8">
<title>KDT Land – Business Card</title>
<link rel="stylesheet" href="https://fonts.googleapis.com/css2?family=Work+Sans:wght@400&display=swap">
<style>
  :root {
    --backdrop: #1c1c1d;
    --card: #151516;
    --card-edge: #232324;
    --name-front: #c9c9ca;
    --tagline-front: #8d8d8f;
    --name-back: #48484a;
    --divider: #8a8a8c;
    --text-strong: #f1f1f1;
    --text-soft: #cfcfd0;
    --text-muted: #9a9a9c;
  }
  * { margin: 0; padding: 0; box-sizing: border-box; }
  html, body { width: 1200px; height: 900px; overflow: hidden; }
  body {
    background: var(--backdrop);
    display: flex;
    flex-direction: column;
    align-items: center;
    justify-content: center;
    gap: 40px;
    font-family: "Work Sans", Arial, sans-serif;
    font-weight: 400;
  }
  .card {
    position: relative;
    width: 700px;
    height: 400px;
    background: radial-gradient(ellipse at 75% 60%, #222224 0%, var(--card) 70%);
    border: 1px solid var(--card-edge);
    overflow: hidden;
  }
  .company-name { display: block; line-height: 1; }
  .company-line { display: block; letter-spacing: 0.5px; }

  .card-front {
    display: flex;
    flex-direction: column;
    align-items: center;
    justify-content: center;
  }
  .card-front .company-name { font-size: 72px; color: var(--name-front); }
  .card-front .company-line { font-size: 17px; color: var(--tagline-front); margin-top: 18px; }

  .card-back .company { position: absolute; left: 50px; top: 160px; width: 290px; }
  .card-back .company-name { font-size: 44px; color: var(--name-back); }
  .card-back .company-line { font-size: 12px; color: var(--name-back); margin-top: 12px; }

  .divider {
    position: absolute; left: 375px; top: 95px;
    width: 2px; height: 210px; background: var(--divider);
  }
  .contact { position: absolute; left: 410px; top: 92px; }
  .contact-name { font-size: 25px; color: var(--text-strong); letter-spacing: 1px; line-height: 1.1; }
  .contact-role { font-size: 14px; color: var(--text-muted); letter-spacing: 1px; margin-bottom: 18px; }
  .contact-address { font-size: 15.5px; color: var(--text-soft); line-height: 1.4; letter-spacing: 0.5px; margin-bottom: 12px; }
  .contact-list { list-style: none; }
  .contact-list li {
    display: flex; align-items: center; gap: 10px;
    font-size: 16px; color: var(--text-soft); letter-spacing: 0.6px; line-height: 1.45;
  }
  .contact-list svg { width: 12px; height: 12px; flex: none; fill: none; stroke: var(--text-muted); stroke-width: 1.4; }
</style>
</head>
<body>
  <section class="card card-front" aria-label="Card front">
    <span class="company-name">KDT Land</span>
    <span class="company-line">Lifestyle property development</span>
  </section>

  <section class="card card-back" aria-label="Card back">
    <div class="company">
      <span class="company-name">KDT Land</span>
      <span class="company-line">Lifestyle property development</span>
    </div>
    <div class="divider"></div>
    <div class="contact">
      <p class="contact-name">OWEN TALLIS</p>
      <p class="contact-role">CEO</p>
      <p class="contact-address">Suite 2207, The Meridale,<br>41 Larchmont Rd.,<br>Central, Hong Kong</p>
      <ul class="contact-list">
        <li>
          <svg viewBox="0 0 12 12" aria-hidden="true"><path d="M2.5 1.5 L4.5 1.5 L5.2 3.8 L4 4.8 Q5 7 7.2 8 L8.2 6.8 L10.5 7.5 L10.5 9.5 Q10.5 10.5 9.5 10.5 Q2 10 1.5 2.5 Q1.5 1.5 2.5 1.5 Z"/></svg>
          + 852 9416 2057
        </li>
        <li>
          <svg viewBox="0 0 12 12" aria-hidden="true"><rect x="3" y="1.5" width="6" height="3"/><rect x="1.5" y="4.5" width="9" height="4"/><rect x="3" y="8.5" width="6" height="2.5"/></svg>
          + 852 3582 0400
        </li>
        <li>
          <svg viewBox="0 0 12 12" aria-hidden="true"><rect x="1" y="2.5" width="10" height="7"/><path d="M1 2.5 L6 6.5 L11 2.5"/></svg>
          owen@kdtland-hq.com
        </li>
      </ul>
    </div>
  </section>
</body>
</html>
```